Youtube Graphic Design for Fitness Brand

I own a personal training/fitness brand called Bright Quarry Fitness. I am starting my YouTube channel and need artwork for my banner and an animated intro/outro. For my banner, I would like to see designs that incorporate my brand logo and one of the attached images of me. The point of my channel is to help educate others and help them achieve their fitness goals to live happy balanced lives. The final design should present a high quality fitness brand that offers value to its subscribers. I'd like to keep the project with either a predominately black or white color. Not sure if I have a preference on either color being the dominant color.

Target Market(s)

People looking for help with fitness/healthy lifestyle.

Industry/Entity Type

Fitness

Requirements
Must have
• My logo
Nice to have
• One of the attached photos of me

```html
<!DOCTYPE html>
<html lang="en">
<head>
<meta charset="UTF-8">
<title>Bright Quarry Fitness — Channel Banner</title>
<link rel="stylesheet" href="https://fonts.googleapis.com/css2?family=Montserrat:wght@700&family=Roboto:wght@400;500&display=swap">
<style>
  :root {
    --page-bg: #ffffff;
    --stage-grey: #cccccc;
    --banner-bg: #000000;
    --brand-white: #ffffff;
    --photo-mid: #5a5a5a;
    --photo-dark: #000000;
    --frame-white: #ffffff;
    --info-bar: #f9f9f9;
    --feed-bg: #f1f1f1;
    --ink: #111111;
    --ink-muted: #606060;
    --tab-ink: #606060;
    --tab-active: #606060;
    --subscribe-red: #cc0000;
  }
  html, body {
    margin: 0;
    padding: 0;
    width: 1200px;
    height: 1200px;
    overflow: hidden;
    background: var(--page-bg);
  }
  .canvas { display: block; width: 1200px; height: 1200px; }
  .brand-name {
    font-family: "Montserrat", sans-serif;
    font-weight: 700;
    fill: var(--brand-white);
  }
  .brand-mark { fill: none; stroke: var(--brand-white); }
  .ui-text { font-family: "Roboto", sans-serif; }
  .channel-title { font-size: 12.5px; fill: var(--ink); }
  .channel-count { font-size: 7px; fill: var(--ink-muted); }
  .subscribe-label { font-size: 7px; font-weight: 500; fill: var(--brand-white); }
  .tab-label { font-size: 6.8px; font-weight: 500; fill: var(--tab-ink); }
  .tab-label--active, .tab-label--strong { fill: var(--ink); }
</style>
</head>
<body>
<svg class="canvas" viewBox="0 0 1200 1200" xmlns="http://www.w3.org/2000/svg" aria-label="Bright Quarry Fitness channel banner and channel page preview">
  <defs>
    <radialGradient id="trainer-tone" cx="50%" cy="45%" r="55%">
      <stop offset="0%" stop-color="var(--photo-mid)"/>
      <stop offset="100%" stop-color="var(--photo-dark)"/>
    </radialGradient>
  </defs>

  <!-- standalone banner -->
  <rect class="page-field" x="0" y="0" width="1200" height="675" fill="var(--page-bg)"/>
  <g class="channel-banner">
    <rect x="0" y="238" width="1200" height="199" fill="var(--banner-bg)"/>
    <circle class="brand-mark" cx="336" cy="332" r="37" stroke-width="5"/>
    <text class="brand-name" x="389" y="335" font-size="33" textLength="305" lengthAdjust="spacing">BRIGHT QUARRY</text>
    <text class="brand-name" x="390" y="356" font-size="16" textLength="176" lengthAdjust="spacing">FITNESS</text>
    <rect x="708" y="252" width="106" height="185" fill="url(#trainer-tone)"
          role="img" aria-label="Black and white photo of the trainer, shirtless, holding a dumbbell in each hand"/>
  </g>

  <!-- channel page preview -->
  <rect class="stage" x="0" y="675" width="1200" height="525" fill="var(--stage-grey)"/>
  <g class="channel-page">
    <rect x="283" y="775" width="634" height="314" fill="var(--frame-white)"/>
    <rect x="285" y="779" width="631" height="104" fill="var(--banner-bg)"/>
    <circle class="brand-mark" cx="461" cy="828" r="19" stroke-width="3"/>
    <text class="brand-name" x="489" y="830" font-size="17" textLength="161" lengthAdjust="spacing">BRIGHT QUARRY</text>
    <text class="brand-name" x="490" y="841" font-size="8" textLength="92" lengthAdjust="spacing">FITNESS</text>
    <rect x="657" y="787" width="56" height="96" fill="url(#trainer-tone)"
          role="img" aria-label="Black and white photo of the trainer holding dumbbells"/>

    <rect x="285" y="883" width="631" height="65" fill="var(--info-bar)"/>
    <circle cx="355" cy="905" r="20" fill="var(--banner-bg)"/>
    <circle class="brand-mark" cx="355" cy="901" r="5" stroke-width="1"/>
    <text class="brand-name" x="355" y="912" font-size="3.2" text-anchor="middle">BRIGHT QUARRY</text>
    <text class="ui-text channel-title" x="387" y="904">Bright Quarry Fitness</text>
    <text class="ui-text channel-count" x="385" y="915">506 rb subscriber</text>
    <rect x="814" y="896" width="50" height="18" rx="1" fill="var(--subscribe-red)"/>
    <text class="ui-text subscribe-label" x="839" y="907.5" text-anchor="middle">SUBSCRIBE</text>

    <text class="ui-text tab-label tab-label--active" x="330" y="939" text-anchor="middle">BERANDA</text>
    <text class="ui-text tab-label" x="384" y="939" text-anchor="middle">VIDEO</text>
    <text class="ui-text tab-label" x="438" y="939" text-anchor="middle">PLAYLIST</text>
    <text class="ui-text tab-label tab-label--strong" x="500" y="939" text-anchor="middle">KOMUNITAS</text>
    <text class="ui-text tab-label" x="563" y="939" text-anchor="middle">CHANNEL</text>
    <text class="ui-text tab-label" x="622" y="939" text-anchor="middle">TENTANG</text>
    <g class="search-icon" fill="none" stroke="var(--tab-ink)" stroke-width="1">
      <circle cx="671" cy="935.5" r="2.8"/>
      <line x1="673" y1="937.5" x2="675.5" y2="940"/>
    </g>
    <polyline points="901,934 904,937 901,940" fill="none" stroke="var(--ink)" stroke-width="1"/>
    <rect x="300" y="946" width="60" height="1.5" fill="var(--tab-active)"/>

    <rect x="286" y="948" width="631" height="141" fill="var(--feed-bg)"/>
    <rect x="300" y="1088" width="199" height="1" fill="var(--ink-muted)"/>
  </g>
</svg>
</body>
</html>
```